Website design for Maple Nook Kidcare

I need a website designed for my daycare business, Maple Nook Kidcare, now that I have a new logo. My former website was ok but simple and I did not have a logo yet. It also was created by me using a template and was entirely pink. I loved the bright, happy feel of it but worried it might not appeal as much to potential clients who have sons. Therefore, I need a site which will appeal to both genders while still keeping the cheerful color scheme of my new logo, which has pinks, blue, green and cream.

Reason: Hello! I am still trying to download my new logo and am sorry it is taking me so long. Hopefully I will it posted by the end of today (US Eastern Standard Time). Thank you all very much for your patience!

Hello! I have finally managed to upload my new logo for you to use in designing my website. I'm sorry it took so long and greatly appreciate your time and creative efforts! I look forward to seeing what is submitted based on my logo design and its style/colors.

Many thanks!

Reason: As I've been traveling and posted my logo file late, I am extending my deadline. I am now back and can focus on providing more and better feedback. I appreciate your patience and submissions very much!

Reason: I need more time to provide feedback and make decisions.

Industry/Entity Type

Daycare

Colors
0192cd
33a6d7
86cae7
cadf82
fbf289
add136
e34197

```html
<!DOCTYPE html>
<html lang="en">
<head>
<meta charset="utf-8">
<title>Maple Nook Kidcare</title>
<link rel="stylesheet" href="https://fonts.googleapis.com/css2?family=Gelasio:wght@400;600&family=Open+Sans:wght@400&display=swap">
<style>
  :root {
    --sky: #6fbde9;
    --sky-light: #bfe4f7;
    --page: #f9f9f9;
    --pink: #f33f5f;
    --green: #53ab24;
    --cream: #f3eb9d;
    --ink: #3a3a3a;
    --body: #444444;
    --white: #ffffff;
  }
  * { margin: 0; padding: 0; box-sizing: border-box; }
  html, body { width: 980px; height: 1200px; overflow: hidden; }
  body {
    position: relative;
    background: radial-gradient(ellipse 520px 360px at 50% 0%, var(--sky-light), var(--sky) 100%);
    background-color: var(--sky);
    font-family: "Open Sans", Arial, sans-serif;
    color: var(--body);
  }
  .page {
    position: absolute; left: 128px; top: 39px; width: 724px; height: 1064px;
    background: var(--page);
  }
  .brand {
    position: absolute; left: 8px; top: 9px;
    font-family: "Gelasio", Georgia, serif; font-size: 26px; font-weight: 400;
    color: var(--pink); letter-spacing: 0.2px;
  }
  .phone {
    position: absolute; right: 9px; top: 36px;
    font-family: "Gelasio", Georgia, serif; font-size: 15px; color: var(--ink);
    display: flex; align-items: center; gap: 3px;
  }
  .nav {
    position: absolute; left: 8px; top: 61px; width: 708px; height: 43px;
    background: var(--pink); display: flex;
    font-family: "Gelasio", Georgia, serif; font-size: 14px; color: var(--white);
  }
  .nav a { display: flex; align-items: center; padding: 0 14.6px; color: inherit; text-decoration: none; }
  .nav a.active { background: var(--green); padding: 0 28px; }
  .hero {
    position: absolute; left: 8px; top: 104px; width: 708px; height: 270px;
    background: linear-gradient(100deg, #7cc3e3 0%, #e9d6b8 30%, #f3e6a4 55%, #f2c9b9 80%, #cfd6d3 100%);
  }
  .dots { position: absolute; left: 334px; top: 245px; display: flex; gap: 5px; }
  .dots span { width: 12px; height: 12px; border-radius: 50%; background: var(--white); }
  .dots span.on { background: var(--green); }
  .welcome {
    position: absolute; left: 8px; top: 392px; width: 708px; text-align: center;
  }
  .welcome h1 {
    font-family: "Gelasio", Georgia, serif; font-weight: 400; font-size: 19px;
    line-height: 29px; color: var(--pink);
  }
  .welcome p { font-size: 10.3px; line-height: 21px; margin-top: 5px; }
  .welcome p + p { margin-top: 12px; }
  .news {
    position: absolute; left: 8px; top: 590px; width: 708px; height: 83px;
    background: var(--cream);
  }
  .news h2 {
    position: absolute; left: 13px; top: 20px;
    font-family: "Gelasio", Georgia, serif; font-weight: 400; font-size: 33px; color: var(--pink);
  }
  .news p { position: absolute; left: 121px; top: 13px; width: 570px; font-size: 10.3px; line-height: 18.4px; }
  .offer-title {
    position: absolute; left: 8px; top: 694px; width: 708px; text-align: center;
    font-family: "Gelasio", Georgia, serif; font-weight: 400; font-size: 22px; color: var(--ink);
  }
  .card { position: absolute; top: 744px; width: 226px; text-align: center; }
  .card .photo { width: 226px; height: 143px; }
  .card h3 {
    margin-top: 10px; font-family: "Gelasio", Georgia, serif; font-weight: 600;
    font-size: 12.5px; color: var(--ink); letter-spacing: 0.3px;
  }
  .card p { margin-top: 9px; font-size: 10.3px; line-height: 18px; padding: 0 10px; height: 54px; }
  .card .more {
    display: inline-block; margin-top: 6px; width: 80px; height: 27px; line-height: 27px;
    background: var(--pink); color: var(--white);
    font-family: "Gelasio", Georgia, serif; font-size: 10.5px;
  }
  .footer-nav {
    position: absolute; left: 148px; top: 1119px; width: 696px;
    display: flex; justify-content: space-between;
    font-family: "Gelasio", Georgia, serif; font-size: 14px; color: var(--white);
  }
  .copyright {
    position: absolute; left: 0; top: 1150px; width: 980px; text-align: center;
    font-family: "Gelasio", Georgia, serif; font-size: 13px; color: var(--white);
  }
</style>
</head>
<body>
  <div class="page">
    <div class="brand">Maple Nook Kidcare</div>
    <div class="phone">
      <svg width="12" height="14" viewBox="0 0 12 14" aria-hidden="true"><path d="M3 1 L5 4 L3.8 5.5 C4.5 7.5 5.5 8.8 7.3 10 L8.8 8.8 L11.5 11 L10 13.2 C5.5 12.8 1.2 7.5 1 2.5 Z" fill="#3a3a3a"/></svg>
      (555) 014-2378
    </div>
    <nav class="nav">
      <a class="active">Home</a><a>About Us</a><a>Services</a><a>Hours &amp; Fees</a><a>Policies</a><a>Contact Us</a><a>Photos</a><a>Testimonials</a>
    </nav>
    <div class="hero" role="img" aria-label="Photo of smiling young children huddled together outdoors">
      <div class="dots"><span class="on"></span><span></span><span></span><span></span></div>
    </div>
    <section class="welcome">
      <h1>Welcome to Maple Nook Kidcare, a playspace where children can play,<br>create, and imagine!</h1>
      <p>Welcome to Maple Nook Kidcare, a licensed Group Family Day Care, located in Riverton's beautiful Hillside district. We are located on a pretty, tree-lined block on Alder Street, between Birch and Cedar Avenues. We are a few blocks from the Green Line train and the Elm Road bus route, and we offer flexible hourly childcare, making it as easy as possible for busy parents on the go to arrange their children's care.</p>
      <p>We invite you to learn more about us and hope you will visit us soon!</p>
    </section>
    <section class="news">
      <h2>News</h2>
      <p>We are thrilled to have found a new cheerful space with a private backyard! It's large, sunny, and filled with outdoor play equipment such as a toddler slide, sand/water activity table, and lots of toys! Please stay tuned for updates on our program and services as we say goodbye to Winter and hello to Spring!</p>
    </section>
    <h2 class="offer-title">What We Offer</h2>
    <div class="card" style="left:8px">
      <div class="photo" role="img" aria-label="Photo of smiling children at a classroom desk" style="background:linear-gradient(110deg,#8cc6e6,#f1d3b0 50%,#5b8fd0)"></div>
      <h3>LEARNING</h3>
      <p>We develop age-appropriate activities that introduce and strengthen academic and social skills.</p>
      <span class="more">Read More</span>
    </div>
    <div class="card" style="left:249px">
      <div class="photo" role="img" aria-label="Photo of a child with paint-covered hands" style="background:linear-gradient(110deg,#e9453c,#f4d9b8 45%,#f0f0f0 70%,#3d7fcf)"></div>
      <h3>CREATIVITY</h3>
      <p>We offer children a wide range of creative opportunities including art projects, tod-dler yoga lessons, afternoon</p>
      <span class="more">Read More</span>
    </div>
    <div class="card" style="left:490px">
      <div class="photo" role="img" aria-label="Photo of two toddlers playing with building blocks" style="background:linear-gradient(170deg,#ffffff 40%,#e8ddc9 75%,#d99a4a)"></div>
      <h3>SHARING</h3>
      <p>We strive to include enrichment activities that extend your child's understanding of the world and their role in it.</p>
      <span class="more">Read More</span>
    </div>
  </div>
  <nav class="footer-nav">
    <span>Home</span><span>|</span><span>About Us</span><span>|</span><span>Services</span><span>|</span><span>Hours &amp; Fees</span><span>|</span><span>Policies</span><span>|</span><span>Contact Us</span><span>|</span><span>Photos</span><span>|</span><span>Testimonials</span>
  </nav>
  <div class="copyright">© 2014 Compnay Name ,All Rights Reserved</div>
</body>
</html>
```